Awesome Digital Ad Design – Quorvex Remarketing

I am going to be setting up a Quorvex Remarketing ad campaign I need creatives for.

Several sizes are needed in the end, however, please submit your design concept in the following 2 sizes to start:
Medium rectangle: 300X250
Leaderboard: 728X90

Original artwork/design files and images used expected upon payment and as part of the final delivery.

Ads should match our company brand and the information on this webpage: http://www.brightlanesystems.com/real-estate-marketing/
SEE MORE INSTRUCTIONS IN ATTACHED WORD DOC
Updates

Project Deadline Extended Reason: Extending deadline to designers hoping to receive more design concept options. Thanks to everyone who has already submitted! Added Wednesday, February 8, 2017

Target Market(s)

Business-To-Business Audience –Real Estate Company Executives (Presidents/VPs/Owners/CEOs/Sales Managers).

Industry/Entity Type

Real Estate

Font styles to use
Sans Serif

Requirements
Must have
• Copy should be minimal words, billboard like. Please use real photos/images that would appeal to real estate high-level decision-maker executives.
Should not have
• No cartoons or graphics

```html
<!DOCTYPE html>
<html lang="en">
<head>
<meta charset="utf-8">
<title>Client Follow-Up Made Simple – Ad Set</title>
<link rel="stylesheet" href="https://fonts.googleapis.com/css2?family=Lato:wght@400;700;900&display=swap">
<style>
  :root {
    --stage: #e6e6e6;
    --panel: #ffffff;
    --headline: #4a6d88;
    --body-text: #666a6e;
    --brand-text: #6d7277;
    --action: #ec6a1f;
    --action-text: #ffffff;
    --photo-light: #eef3f4;
    --photo-mid: #c9d8e2;
    --photo-deep: #9fb7c8;
  }
  * { box-sizing: border-box; margin: 0; padding: 0; }
  html, body { width: 1200px; height: 1200px; overflow: hidden; }
  body { background: var(--stage); font-family: "Lato", sans-serif; }
  .canvas { position: relative; width: 1200px; height: 1200px; }

  .ad { position: absolute; background: var(--panel); overflow: hidden; }
  .ad__headline {
    position: absolute; color: var(--headline); font-weight: 900;
    letter-spacing: -0.01em; line-height: 1.2; text-transform: uppercase;
  }
  .ad__brand {
    position: absolute; color: var(--brand-text); font-weight: 400;
    line-height: 1.25;
  }
  .ad__tagline { position: absolute; color: var(--body-text); font-weight: 400; }
  .ad__button {
    position: absolute; display: flex; align-items: center; justify-content: center;
    background: var(--action); color: var(--action-text); font-weight: 700;
    border-radius: 4px; letter-spacing: -0.02em;
  }
  .ad__photo { position: absolute; }

  /* Leaderboard 728×90 */
  .ad--leaderboard { left: 125px; top: 148px; width: 950px; height: 131px; }
  .ad--leaderboard .ad__headline { left: 42px; top: 31px; font-size: 32px; }
  .ad--leaderboard .ad__brand { left: 393px; top: 46px; font-size: 15px; }
  .ad--leaderboard .ad__tagline {
    left: 540px; top: 22px; width: 194px; text-align: center;
    font-size: 22px; line-height: 1.15;
  }
  .ad--leaderboard .ad__button { left: 601px; top: 84px; width: 90px; height: 26px; font-size: 16px; }
  .ad--leaderboard .ad__photo {
    left: 741px; top: 8px; width: 202px; height: 115px;
    background: linear-gradient(90deg, var(--photo-light) 0%, var(--photo-mid) 45%, var(--photo-deep) 100%);
  }

  /* Medium rectangle 300×250 */
  .ad--rectangle { left: 332px; top: 510px; width: 743px; height: 620px; }
  .ad--rectangle .ad__photo {
    left: 264px; top: 266px; width: 468px; height: 344px;
    background: linear-gradient(90deg, var(--panel) 0%, var(--photo-light) 22%, var(--photo-mid) 60%, var(--photo-deep) 100%);
  }
  .ad--rectangle .ad__headline { left: 60px; top: 92px; font-size: 46px; line-height: 1.1; }
  .ad--rectangle .ad__brand { left: 532px; top: 118px; font-size: 22px; }
  .ad--rectangle .ad__tagline { left: 60px; top: 338px; font-size: 42px; line-height: 1.2; letter-spacing: -0.01em; }
  .ad--rectangle .ad__button { left: 59px; top: 529px; width: 171px; height: 49px; font-size: 29px; }
</style>
</head>
<body>
<main class="canvas">

  <section class="ad ad--leaderboard" aria-label="Leaderboard ad, 728 by 90">
    <h1 class="ad__headline">Client Follow-Up<br>Made Simple</h1>
    <p class="ad__brand">Brightlane<br>Systems</p>
    <p class="ad__tagline">Virtually No Cost To Your Company!</p>
    <a class="ad__button" href="#">Learn More</a>
    <div class="ad__photo" role="img" aria-label="Photo of two smiling business colleagues reviewing a laptop in a bright office"></div>
  </section>

  <section class="ad ad--rectangle" aria-label="Medium rectangle ad, 300 by 250">
    <div class="ad__photo" role="img" aria-label="Photo of two smiling business colleagues reviewing a laptop in a bright office"></div>
    <h2 class="ad__headline">Client Follow-Up<br>Made Simple</h2>
    <p class="ad__brand">Brightlane<br>Systems</p>
    <p class="ad__tagline">Virtually No<br>Cost To Your<br>Company!</p>
    <a class="ad__button" href="#">Learn More</a>
  </section>

</main>
</body>
</html>
```